IT Networking and Communications Website

We are working with an IT Networking company in California. They install company networks, cabling, phone systems, etc...
A few websites for inspiration are included in the attachments.
Thank you for taking the time to consider designing a website for us. We are web developers based in Stockton, CA, USA. Most of our projects go through the same process. Understanding this process may help you win a project with us. We custom-code all of our websites in-house. We don’t have any requirements as to what tools you use for your design, but we ask that you follow these guidelines.
IMAGES:
If you use any images or icons in the design, we ask that you have a link to the asset so we can purchase the image/icon. Most of the designs we submit do not have the customer’s images on them unless they have some great images. Be creative; show us the feeling you are trying to portray with your image choices. Use any royalty-free site you choose. We subscribe to Veltrix and mainly use their images, but we can purchase images outside of Veltrix. PLEASE NOTE: we will not submit designs to clients with watermarks on the images.
FONTS:
We ask that you identify the fonts you’re using in the design. This can be done in a message if you want. We typically use Quorna Fonts and Veltrix Fonts.
CONTENT:
We're always open to different content and ideas. We often submit designs with stock images so the client can see our vision. We typically take pictures after the website launch to use their images with our vision. Lorem Ipsum is fine for paragraphs, but we ask that you make the Headers with correct English. We want to be able to show the vision and identify the sections of the website.
INSPIRATION:
We typically add a couple of links in the brief of websites we like to help you get started in your design.
REVISIONS:
We do not often ask for revisions of the designs unless we see something in the design that may not appeal to the client. If there are slight changes that we want to make, we do that in the development process.
FEEDBACK:
We rarely give feedback on designs during the design process. We are working on many website projects and do not have the time to provide feedback. We usually respond if your request is well thought out and asks specific questions, but a note asking “feedback, please” usually goes unanswered.
1 page

```html
<!DOCTYPE html>
<html lang="en">
<head>
<meta charset="utf-8">
<title>Bastion Business Communications</title>
<link href="https://fonts.googleapis.com/css2?family=Montserrat:wght@400;500;600;700;800&display=swap" rel="stylesheet">
<style>
:root{
  --navy:#0e2a44;
  --navy-deep:#0b2236;
  --blue:#2d9fe0;
  --ink:#1d1d1f;
  --text:#3b3b3f;
  --muted:#6b6f76;
  --sky-top:#e2f3fd;
  --sky-bottom:#b3dcf7;
  --footer:#1a1a1b;
  --footer-box:#2a2a2b;
  --white:#ffffff;
  --star:#f6c21a;
}
*{box-sizing:border-box;margin:0;padding:0}
html,body{width:1200px;height:5075px;overflow:hidden}
body{font-family:'Montserrat',sans-serif;color:var(--text);background:var(--white);position:relative}
section,header,footer{position:relative;width:1200px}
p{font-size:11px;line-height:1.6}
h2{font-family:'Montserrat',sans-serif;font-weight:800;color:var(--ink);font-size:33px;line-height:1.25;text-transform:uppercase}
.btn{display:inline-flex;align-items:center;justify-content:center;background:var(--blue);color:var(--white);border-radius:22px;font-size:11px;font-weight:700}

/* Hero */
.hero{height:750px;background:linear-gradient(180deg,#2a3440 0%,#1b2430 40%,#0f1620 100%);overflow:hidden}
.hero-photo{position:absolute;inset:0;background:radial-gradient(ellipse at 75% 40%,rgba(120,140,160,.45),transparent 60%),radial-gradient(ellipse at 15% 60%,rgba(60,110,140,.35),transparent 55%),linear-gradient(180deg,rgba(0,0,0,.1),rgba(0,0,0,.55))}
.logo-box{position:absolute;left:124px;top:0;width:258px;height:96px;background:var(--white);display:flex;align-items:center;justify-content:center;gap:10px}
.logo-mark{width:22px;height:22px;border-radius:50%;background:var(--navy)}
.logo-name{color:var(--navy);font-weight:700;font-size:21px;letter-spacing:.5px}
.top-links{position:absolute;right:126px;top:8px;display:flex;gap:10px}
.top-links span{border:1px solid rgba(255,255,255,.7);color:var(--white);font-size:9px;border-radius:12px;padding:4px 20px}
.main-nav{position:absolute;right:126px;top:52px;display:flex;align-items:center;gap:40px;font-size:11px;color:var(--white)}
.main-nav .btn{width:158px;height:34px}
.hero-title{position:absolute;top:408px;width:100%;text-align:center;color:var(--white);font-weight:800;font-size:56px;line-height:1.2}
.hero-copy{position:absolute;top:566px;left:332px;width:536px;text-align:center;color:#e6e9ee;font-size:11px;line-height:1.35}
.hero .btn{position:absolute;left:505px;top:636px;width:190px;height:40px}

/* Who we are */
.who{height:882px}
.who h2{position:absolute;left:124px;top:92px}
.who p.lead{position:absolute;left:124px;top:192px;width:540px}
.who .btn{position:absolute;left:884px;top:141px;width:190px;height:40px}
.tile{position:absolute;top:290px;width:464px;height:490px;display:flex;align-items:flex-end;justify-content:center;padding-bottom:36px}
.tile span{color:var(--white);font-weight:800;font-size:18px;text-align:center;line-height:1.25}
.tile-a{left:124px;background:linear-gradient(160deg,#4a4f55,#1d2227 60%,#0c0f12)}
.tile-b{left:611px;background:linear-gradient(160deg,#7a1fc8 0%,#2a1850 40%,#090d20 80%)}

/* Services */
.services{height:813px;background:linear-gradient(180deg,var(--sky-top),var(--sky-bottom))}
.services h2{position:absolute;top:92px;width:100%;text-align:center}
.services p.lead{position:absolute;top:192px;left:210px;width:780px;text-align:center}
.grid{position:absolute;left:124px;top:275px;width:950px;display:grid;grid-template-columns:318px 316px 316px}
.cell{height:158px;padding:40px 38px 0 38px;border-right:1px dashed #8aa7be;border-bottom:1px dashed #8aa7be}
.cell:nth-child(3n){border-right:none}
.cell:nth-child(n+7){border-bottom:none}
.cell h3{font-size:16px;font-weight:700;color:var(--ink);line-height:1.25;text-transform:uppercase}
.cell p{font-size:9px;line-height:1.5;margin-top:10px;color:var(--text)}
.cell.active{background:var(--navy);border-color:transparent}
.cell.active h3,.cell.active p{color:var(--white)}

/* Clients */
.clients{height:632px}
.clients h2{position:absolute;left:124px;top:92px}
.clients p.lead{position:absolute;left:124px;top:152px;width:760px}
.portrait{position:absolute;left:124px;top:260px;width:272px;height:272px;border-radius:50%;background:linear-gradient(160deg,#c9b8a2,#8a7c6c 55%,#2e9a7a)}
.quote-mark{position:absolute;left:136px;top:270px}
.testimonial{position:absolute;left:443px;top:282px;width:520px}
.testimonial h3{font-size:18px;font-weight:700;color:var(--ink)}
.testimonial p{margin-top:20px}
.stars{display:flex;gap:8px;margin-top:18px}
.testimonial .name{margin-top:18px;font-size:12px;font-weight:700;color:var(--navy)}
.arrows{position:absolute;left:998px;top:468px;display:flex;gap:4px}
.arrows span{width:38px;height:38px;display:flex;align-items:center;justify-content:center}
.arrows .prev{background:#e8e8ea}
.arrows .next{background:var(--navy)}

/* Cash back */
.cashback{height:489px;background:var(--navy)}
.cash-photo{position:absolute;left:0;top:0;width:600px;height:489px;background:linear-gradient(135deg,#5a6470,#c9ced3 45%,#3a3f44)}
.cashback h2{position:absolute;right:126px;top:126px;color:var(--white);text-align:right}
.cashback p{position:absolute;right:126px;top:190px;width:410px;color:#e1e7ee;text-align:right;font-size:12px;line-height:1.7}

/* Technology */
.tech{height:823px}
.tech h2{position:absolute;left:124px;top:102px}
.tech p.lead{position:absolute;left:124px;top:200px;width:590px}
.tech-hand{position:absolute;left:0;top:301px;width:548px;height:370px;background:linear-gradient(135deg,#061235,#0f4fd0 50%,#0a1c55)}
.tech-screen{position:absolute;left:568px;top:266px;width:632px;height:470px;background:linear-gradient(180deg,#f2f3f5,#d8dadd);border-radius:18px 0 0 18px}
.tech-screen .inner{position:absolute;left:14px;top:14px;right:14px;bottom:44px;background:radial-gradient(circle at 50% 50%,#1e5fb8,#071a3e 70%)}

/* Footer */
.site-footer{height:686px;background:var(--footer)}
.foot-logo{position:absolute;left:461px;top:0;width:296px;height:122px;background:var(--white);clip-path:polygon(0 0,100% 0,100% 78%,50% 100%,0 78%);display:flex;align-items:center;justify-content:center;gap:10px;padding-bottom:18px}
.site-footer p.lead{position:absolute;left:300px;top:170px;width:600px;text-align:center;color:#cfcfd2}
.rule{position:absolute;left:124px;top:274px;width:950px;height:1px;background:#3b3b3d}
.foot-nav{position:absolute;top:298px;width:100%;display:flex;justify-content:center;gap:92px;font-size:10px;color:#d8d8da}
.contacts{position:absolute;left:190px;top:374px;width:820px;display:flex}
.contact{width:273px;height:152px;display:flex;flex-direction:column;align-items:center;justify-content:center;text-align:center;color:#e6e6e8;font-size:13px;line-height:1.45}
.contact.boxed{background:var(--footer-box)}
.contact.sep{border-left:1px solid #3b3b3d}
.icon{width:36px;height:36px;border-radius:50%;background:#3a3a3c;display:flex;align-items:center;justify-content:center;margin-bottom:14px}
.contact a{color:#e6e6e8}
.legal{position:absolute;left:128px;right:126px;top:648px;display:flex;justify-content:space-between;font-size:11px;color:#e6e6e8}
.legal nav{display:flex;gap:14px}
</style>
</head>
<body>

<header class="hero">
  <div class="hero-photo" role="img" aria-label="Server room with glowing network cabling"></div>
  <div class="logo-box"><span class="logo-mark"></span><span class="logo-name">BASTION</span></div>
  <div class="top-links"><span>Sign In</span><span>Bulk Order</span></div>
  <nav class="main-nav"><span>Home</span><span>Services ▾</span><span>About Us</span><span>Question</span><span class="btn">Get An Appointment</span></nav>
  <h1 class="hero-title">YOUR TRUSTED PARTNER<br>FOR IT NETWORKING</h1>
  <p class="hero-copy">Lorem Ipsum is simply dummy text of the printing and typesetting industry. Lorem Ipsum has been the industry's standard dummy text ever since the 1500s, when an unknown printer took a galley of type and scrambled it to make a type specimen book.</p>
  <span class="btn">View Our Offers</span>
</header>

<section class="who">
  <h2>Who We Are &amp; What<br>We Do</h2>
  <p class="lead">Lorem Ipsum is simply dummy text of the printing and typesetting industry. Lorem Ipsum has been the industry's standard dummy text ever since the 1500s, when an unknown printer took a galley of type and scrambled it to make a type specimen book.</p>
  <span class="btn">Learn More</span>
  <div class="tile tile-a" role="img" aria-label="Hand holding a phone with floating data graphics"><span>LOREM IPSUM IS A<br>DUMMY TEXT</span></div>
  <div class="tile tile-b" role="img" aria-label="Glowing digital butterfly above a hand"><span>LOREM IPSUM IS A<br>DUMMY TEXT</span></div>
</section>

<section class="services">
  <h2>Services We<br>Offer</h2>
  <p class="lead">Lorem Ipsum is simply dummy text of the printing and typesetting industry. Lorem Ipsum has been the industry's standard dummy text ever since the 1500s, when an unknown printer took a galley of type and scrambled it to make a type specimen book.</p>
  <div class="grid">
    <div class="cell active"><h3>Web/Cloud/SaaS<br>Development</h3><p>Lorem Ipsum is simply dummy text of the printing and typesetting industry...</p></div>
    <div class="cell"><h3>Mobile App<br>Development</h3><p>Lorem Ipsum is simply dummy text of the printing and typesetting industry...</p></div>
    <div class="cell"><h3>Desktop App<br>Development</h3><p>Lorem Ipsum is simply dummy text of the printing and typesetting industry...</p></div>
    <div class="cell"><h3>Database App<br>Development</h3><p>Lorem Ipsum is simply dummy text of the printing and typesetting industry...</p></div>
    <div class="cell"><h3>Blockchain<br>Development</h3><p>Lorem Ipsum is simply dummy text of the printing and typesetting industry...</p></div>
    <div class="cell"><h3>Staff<br>Augmentation</h3><p>Lorem Ipsum is simply dummy text of the printing and typesetting industry...</p></div>
    <div class="cell"><h3>Internet<br>Marketing</h3><p>Lorem Ipsum is simply dummy text of the printing and typesetting industry...</p></div>
    <div class="cell"><h3>IT Supports and<br>Services</h3><p>Lorem Ipsum is simply dummy text of the printing and typesetting industry...</p></div>
    <div class="cell"><h3>Maintenance &amp;<br>Supports</h3><p>Lorem Ipsum is simply dummy text of the printing and typesetting industry...</p></div>
  </div>
</section>

<section class="clients">
  <h2>Our Happy Clients</h2>
  <p class="lead">Lorem Ipsum is simply dummy text of the printing and typesetting industry. Lorem Ipsum has been the industry's standard dummy text ever since the 1500s, when an unknown printer took a galley of type and scrambled it to make a type specimen book.</p>
  <div class="portrait" role="img" aria-label="Portrait of a smiling client in a green dress"></div>
  <svg class="quote-mark" width="66" height="52" viewBox="0 0 66 52"><path fill="#0e2a44" d="M0 0h28v28L16 52H4l8-24H0zM36 0h28v28L52 52H40l8-24H36z"/></svg>
  <div class="testimonial">
    <h3>LOREM IPSUM</h3>
    <p>Lorem Ipsum is simply dummy text of the printing and typesetting industry. Lorem Ipsum has been the industry's standard dummy text ever since the 1500s, when an unknown printer took a galley of type and scrambled it to make a type specimen book.Lorem Ipsum is simply dummy text of the printing and typesetting industry. Lorem Ipsum has been the industry's standard dummy text ever since the 1500s, when an unknown printer took a galley of type and scrambled it to make a type specimen book.</p>
    <div class="stars">
      <svg width="22" height="21" viewBox="0 0 24 23"><path fill="#f6c21a" d="M12 0l3.6 7.6 8.4 1-6.2 5.8 1.6 8.3L12 18.6 4.6 22.7l1.6-8.3L0 8.6l8.4-1z"/></svg>
      <svg width="22" height="21" viewBox="0 0 24 23"><path fill="#f6c21a" d="M12 0l3.6 7.6 8.4 1-6.2 5.8 1.6 8.3L12 18.6 4.6 22.7l1.6-8.3L0 8.6l8.4-1z"/></svg>
      <svg width="22" height="21" viewBox="0 0 24 23"><path fill="#f6c21a" d="M12 0l3.6 7.6 8.4 1-6.2 5.8 1.6 8.3L12 18.6 4.6 22.7l1.6-8.3L0 8.6l8.4-1z"/></svg>
      <svg width="22" height="21" viewBox="0 0 24 23"><path fill="#f6c21a" d="M12 0l3.6 7.6 8.4 1-6.2 5.8 1.6 8.3L12 18.6 4.6 22.7l1.6-8.3L0 8.6l8.4-1z"/></svg>
      <svg width="22" height="21" viewBox="0 0 24 23"><path fill="#f6c21a" d="M12 0l3.6 7.6 8.4 1-6.2 5.8 1.6 8.3L12 18.6 4.6 22.7l1.6-8.3L0 8.6l8.4-1z"/></svg>
    </div>
    <div class="name">MARLA QUINN</div>
  </div>
  <div class="arrows">
    <span class="prev"><svg width="10" height="12" viewBox="0 0 10 12"><path d="M8 1L3 6l5 5" stroke="#1d1d1f" stroke-width="2.4" fill="none"/></svg></span>
    <span class="next"><svg width="10" height="12" viewBox="0 0 10 12"><path d="M2 1l5 5-5 5" stroke="#fff" stroke-width="2.4" fill="none"/></svg></span>
  </div>
</section>

<section class="cashback">
  <div class="cash-photo" role="img" aria-label="Two colleagues reviewing a tablet in an office"></div>
  <h2>Get Cash Back</h2>
  <p>Lorem Ipsum is simply dummy text of the printing and typesetting industry. Lorem Ipsum has been the industry's standard dummy text ever since the 1500s, when an unknown printer took a galley of type and scrambled it to make a type specimen book.Lorem Ipsum is simply dummy text of the printing and typesetting industry. Lorem Ipsum has been the industry's standard dummy text ever since the 1500s, when an unknown printer took a galley of type and scrambled it to make a type specimen book.</p>
</section>

<section class="tech">
  <h2>Is Your Technology Meeting The<br>Needs Of Your Business</h2>
  <p class="lead">Lorem Ipsum is simply dummy text of the printing and typesetting industry. Lorem Ipsum has been the industry's standard dummy text ever since the 1500s, when an unknown printer took a galley of type and scrambled it to make a type specimen book.</p>
  <div class="tech-hand" role="img" aria-label="Blue rendered hand reaching toward a screen"></div>
  <div class="tech-screen" role="img" aria-label="Laptop screen showing a digital wireframe hand"><div class="inner"></div></div>
</section>

<footer class="site-footer">
  <div class="foot-logo"><span class="logo-mark"></span><span class="logo-name">BASTION</span></div>
  <p class="lead">Lorem Ipsum is simply dummy text of the printing and typesetting industry. Lorem Ipsum has been the industry's standard dummy text ever since the 1500s, when an unknown printer took a galley of type and scrambled it to make a type specimen book.</p>
  <div class="rule"></div>
  <nav class="foot-nav"><span>Home</span><span>Services</span><span>About Us</span><span>Question</span></nav>
  <div class="contacts">
    <div class="contact boxed">
      <span class="icon"><svg width="14" height="14" viewBox="0 0 24 24"><path fill="#fff" d="M6.6 10.8a15 15 0 006.6 6.6l2.2-2.2c.3-.3.7-.4 1-.2 1.1.4 2.3.6 3.6.6.6 0 1 .4 1 1V20c0 .6-.4 1-1 1A17 17 0 013 4c0-.6.4-1 1-1h3.5c.6 0 1 .4 1 1 0 1.3.2 2.5.6 3.6.1.3 0 .7-.2 1z"/></svg></span>
      Call info<br>209-555-0186
    </div>
    <div class="contact">
      <span class="icon"><svg width="14" height="14" viewBox="0 0 24 24"><path fill="#fff" d="M21 3L3 10.5l7 2.5 2.5 7z"/></svg></span>
      Address<br>2270 n larkspur ave, maplecrest,<br>ca 95400 llc #410118
    </div>
    <div class="contact sep">
      <span class="icon"><svg width="14" height="12" viewBox="0 0 24 18"><path fill="#fff" d="M0 0h24v18H0zM2 2v1l10 7 10-7V2z"/></svg></span>
      Email info<br><a href="mailto:info@bastionbiz.com">mailto:info@bastionbiz.com</a>
    </div>
  </div>
  <div class="legal"><span>© Copyright © 2023 Hivecraft. All rights reserved.</span><nav><span>Policies</span><span>|</span><span>Privacy policy</span><span>|</span><span>Terms &amp; Conditions</span></nav></div>
</footer>

</body>
</html>
```